flyer for roofing advertising

Need a modern, bold, luxurious advertisement flyer for our roofing company. located in buffalo, ny. Big house with a intense roof design asphalt shingles. slogan is "Reliability starts at the top". Colors varies but want it to be modern. we will be handing these out when we are working in the area. phone number is 716-555-0147 for the NO K.W estimate. also our services are roofing, roof repairs, gutters, attic ventilation. we offer a 15 year warranty with our platinum roof program. We are certified by dwellmatch, harlan trevisk, quarno. Also follow us on linkpage, wexora and frunt. website is ktw-roofing.com, linkpage is ktwroofing. pictures are on linkpage and our website if need more can be provided. also can include a review we have.

```html
<!DOCTYPE html>
<html lang="en">
<head>
<meta charset="utf-8">
<title>KTW Roofing Flyer</title>
<link href="https://fonts.googleapis.com/css2?family=Roboto:wght@300;400;500;700;900&display=swap" rel="stylesheet">
<style>
  :root {
    --orange: #f7a233;
    --orange-deep: #f39a22;
    --ink: #2b2b2b;
    --panel: #8b8b8b;
    --white: #ffffff;
    --stage: #3b3734;
  }
  * { margin: 0; padding: 0; box-sizing: border-box; }
  html, body { width: 1200px; height: 1200px; overflow: hidden; background: var(--stage); }
  body { font-family: "Roboto", Arial, sans-serif; color: var(--white); position: relative; }

  .flyer {
    position: absolute; left: 167px; top: 40px;
    width: 1007px; height: 1302px;
    transform: scale(0.86); transform-origin: 0 0;
    overflow: hidden; background: var(--panel);
    box-shadow: 0 18px 40px rgba(0,0,0,.45);
  }
  .abs { position: absolute; }

  .top-band { left: 0; top: 0; width: 100%; height: 76px; background: var(--orange); }
  .hero-photo {
    left: 0; top: 76px; width: 100%; height: 540px;
    background: linear-gradient(160deg, #3e4650 0%, #5a6470 40%, #6c7582 60%, #48505a 100%);
  }
  .quote { right: 68px; top: 14px; color: var(--ink); display: flex; align-items: baseline; gap: 12px; }
  .quote-label { font-weight: 500; font-size: 20px; letter-spacing: .2px; }
  .quote-number { font-weight: 700; font-size: 45px; letter-spacing: .5px; }

  .brand-tag {
    left: 63px; top: 0; width: 270px; height: 190px; background: var(--white);
    clip-path: polygon(0 0, 100% 0, 100% 100%, 50% 79%, 0 100%);
    text-align: center; padding-top: 46px;
  }
  .brand-name { font-weight: 700; font-size: 58px; color: #8c8c8c; letter-spacing: 4px; line-height: 1; }
  .brand-line { font-weight: 400; font-size: 13px; color: var(--orange-deep); letter-spacing: .6px; margin-top: 14px; }

  .headline { left: 63px; top: 262px; font-weight: 700; font-size: 53px; white-space: nowrap; letter-spacing: -.3px; }
  .headline .accent { color: var(--orange); font-size: 78px; font-weight: 900; }

  .shapes { left: 0; top: 0; width: 1007px; height: 1302px; }

  .photo { left: 0; width: 478px; }
  .photo-roofer { top: 461px; height: 239px; clip-path: polygon(0 50px, 478px 0, 478px 100%, 0 100%);
    background: linear-gradient(135deg, #4f6b45 0%, #6a8a5a 35%, #3f5b55 60%, #c9ced3 100%); }
  .photo-home { top: 700px; height: 216px;
    background: linear-gradient(180deg, #9aa18f 0%, #6b5a4a 40%, #7a4f3a 65%, #4d6a35 100%); }
  .photo-shingles { top: 996px; height: 170px;
    background: linear-gradient(120deg, #3f5753 0%, #4a6460 50%, #c8cdd4 80%, #dfe3e8 100%); }

  .warranty { left: 0; top: 916px; width: 478px; height: 80px; background: var(--orange); }
  .warranty-title { left: 59px; top: 10px; font-weight: 700; font-size: 41px; letter-spacing: .3px; white-space: nowrap; }
  .warranty-note { right: 18px; top: 50px; font-weight: 300; font-size: 20px; white-space: nowrap; }

  .about { left: 511px; top: 472px; width: 455px; }
  .about-title { font-weight: 700; font-size: 24px; line-height: 30px; }
  .about-title .accent { color: var(--orange); }
  .about-text { font-weight: 300; font-size: 17.5px; line-height: 22.5px; margin-top: 33px; text-align: justify; }
  .about-text + .about-text { margin-top: 22px; }

  .services { left: 511px; top: 862px; width: 460px; }
  .services-title { font-weight: 700; font-size: 24px; }
  .services-title .accent { color: var(--orange); }
  .services-list { display: grid; grid-template-columns: 232px 1fr; list-style: none; margin-top: 16px; font-size: 18px; font-weight: 500; row-gap: 5px; }
  .services-list li::before { content: "• "; }

  .certified { left: 511px; top: 1072px; width: 140px; text-align: right; font-weight: 300; font-size: 19px; line-height: 25px; }
  .cert-rule { left: 664px; top: 1076px; width: 2px; height: 82px; background: var(--orange); }
  .badge { top: 1076px; width: 83px; height: 82px; }
  .badge-dwellmatch { left: 684px; background: var(--white); }
  .badge-trevisk { left: 780px; background: #e2231a; border-radius: 10px; }
  .badge-quarno { left: 874px; background: #e2231a; }

  .contact { color: var(--ink); }
  .footer-head { font-weight: 700; font-size: 20px; top: 1211px; }
  .contact-head { left: 63px; }
  .follow-head { left: 646px; }
  .contact-lines { left: 63px; top: 1244px; font-size: 20px; line-height: 28px; }
  .address { left: 326px; top: 1244px; font-size: 20px; line-height: 28px; }
  .social { left: 646px; top: 1246px; display: flex; gap: 16px; font-size: 19px; font-weight: 500; color: var(--ink); }
  .social-item { display: flex; align-items: center; gap: 6px; }
  .social-dot { width: 14px; height: 14px; border-radius: 50%; background: var(--ink); }
  .hashtag { left: 646px; top: 1276px; font-size: 20px; font-weight: 500; }
</style>
</head>
<body>
<main class="flyer">
  <div class="abs hero-photo" role="img" aria-label="Large two-storey house with steep gabled asphalt shingle roof at dusk"></div>
  <div class="abs top-band"></div>
  <div class="abs quote contact"><span class="quote-label">CALL FOR A QUOTE:</span><span class="quote-number">716-555-0147</span></div>

  <div class="abs brand-tag">
    <div class="brand-name">KTW</div>
    <div class="brand-line">ROOFING-SIDING-STONE</div>
  </div>

  <h1 class="abs headline">RELIABILITY STARTS AT THE <span class="accent">TOP</span></h1>

  <div class="abs photo photo-roofer" role="img" aria-label="Roofer laying green asphalt shingles with a nail gun"></div>
  <div class="abs photo photo-home" role="img" aria-label="Brick house with a newly finished brown shingle roof and evergreen shrubs"></div>
  <div class="abs photo photo-shingles" role="img" aria-label="Roofer installing shingles over underlayment around roof vents"></div>

  <svg class="abs shapes" viewBox="0 0 1007 1302" aria-hidden="true">
    <polygon points="478,461 778,403 1007,531 1007,1302 478,1302" fill="#8b8b8b" fill-opacity="0.96"/>
    <polyline points="0,511 478,461 778,403 1007,536" fill="none" stroke="#ffffff" stroke-width="8"/>
    <polygon points="0,1154 73,1131 1007,1216 1007,1302 0,1302" fill="#f39a22"/>
    <polyline points="0,1150 73,1127 1007,1212" fill="none" stroke="#ffffff" stroke-width="8"/>
  </svg>

  <div class="abs warranty">
    <div class="abs warranty-title">15 YEAR WARRANTY</div>
    <div class="abs warranty-note">with our platinum roof program</div>
  </div>

  <section class="abs about">
    <h2 class="about-title">SINCE 1996,<br>THE <span class="accent">BEST ROOFING CONTRACTOR</span><br>IN WESTERN NEW YORK</h2>
    <p class="about-text">KTW Roofing got its start in 1996. Today, we remain family-owned and -operated by three professionals who have 40 years of combined experience. We’re not only the preferred roofing company for installation, repair, and other services, but we’ve also worked hard to earn the title of Harlan Trevisk Preferred Contractor.</p>
    <p class="about-text">KTW Roofing works with safety and longevity in mind: the safety of you and everyone inside your home or commercial property, and the longevity of your roof.</p>
  </section>

  <section class="abs services">
    <h2 class="services-title">OUR <span class="accent">SERVICES</span></h2>
    <ul class="services-list">
      <li>Roof Installation</li><li>Roof Inspection</li>
      <li>Roof Repair</li><li>Siding Repair</li>
      <li>Re-Roof</li><li>New Siding Installation</li>
      <li>Commercial Roofing</li><li>Gutters</li>
    </ul>
  </section>

  <div class="abs certified">WE ARE<br>CERTIFIED BY</div>
  <div class="abs cert-rule"></div>
  <div class="abs badge badge-dwellmatch" role="img" aria-label="dwellmatch certification badge"></div>
  <div class="abs badge badge-trevisk" role="img" aria-label="harlan trevisk certification badge"></div>
  <div class="abs badge badge-quarno" role="img" aria-label="quarno certification badge"></div>

  <h3 class="abs footer-head contact-head contact">Contact us:</h3>
  <div class="abs contact-lines contact">716-555-0147<br>www.ktw-roofing.com</div>
  <div class="abs address contact">2718 Varden Rd, Lockport,<br>NY 14094</div>
  <h3 class="abs footer-head follow-head contact">Follow us on:</h3>
  <div class="abs social">
    <span class="social-item"><span class="social-dot"></span>linkpage</span>
    <span class="social-item"><span class="social-dot"></span>wexora</span>
    <span class="social-item"><span class="social-dot"></span>frunt</span>
  </div>
  <div class="abs hashtag contact">#ktwroofing</div>
</main>
</body>
</html>
```